We are full service plumbing contractors that are capable of performing all of your plumbing need...

A clean, crisp website that conveys we can handle any plumbing from drain cleaning, repairs, to new construction. But emphasis on Leak detection, under-slab and underground water service leaks, repairs, and reroutes. Leak detection by acoustical, Thermal, or tracer gas , methods.Also emphasize advanced drain cleaning technologies and equipment. Don't just poke ahole in the drain blockage, Clean the pipe, with our High pressure hydrojetters, or Chain knocker drain cables that expand to the width of the pipe being cleaned.

Number of Pages Required

5+ page

Font styles to use
Sans Serif

Requirements
Should not have
• Canned photos

```html
<!DOCTYPE html>
<html lang="en">
<head>
<meta charset="UTF-8">
<title>Clearflow – Plumbing Contractors</title>
<link href="https://fonts.googleapis.com/css2?family=Montserrat:wght@500;600;700&family=Lato:ital,wght@0,400;0,700;1,400;1,700&display=swap" rel="stylesheet">
<style>
:root{
  --sky:#0aa2dd;
  --ocean:#1b74c8;
  --navy:#1f4aa6;
  --ink:#111820;
  --text:#4a4f55;
  --muted:#e4e8eb;
  --paper:#ffffff;
  --field:#f2f2f2;
  --line:#c9ced2;
}
*{margin:0;padding:0;box-sizing:border-box}
html,body{width:1200px;height:3766px;overflow:hidden}
body{position:relative;background:var(--paper);font-family:'Lato',sans-serif;color:var(--text)}
.abs{position:absolute}
.heading{font-family:'Montserrat',sans-serif;font-weight:700;color:var(--ink);text-transform:uppercase;letter-spacing:1px}

/* header */
.topbar{left:477px;top:0;width:723px;height:38px;background:linear-gradient(90deg,var(--sky),var(--navy));border-bottom-left-radius:38px;color:#fff;font-size:15px;display:flex;align-items:center;justify-content:flex-end;gap:50px;padding-right:80px}
.topbar span{display:flex;align-items:center;gap:12px}
.brand{left:78px;top:45px;display:flex;align-items:center;gap:12px;font-family:'Montserrat',sans-serif;font-weight:700;font-size:30px;color:var(--ocean);letter-spacing:1px}
.brand i{width:34px;height:34px;border-radius:50%;background:var(--ocean);display:block}
.nav{left:610px;top:72px;width:515px;display:flex;justify-content:space-between;font-family:'Montserrat',sans-serif;font-size:15px;font-weight:500;color:#333}
.nav .on{color:var(--ocean)}

/* hero */
.hero{left:0;top:125px;width:1200px;height:543px;background:linear-gradient(90deg,#f4f6f8 0%,#e7ecf0 40%,#9fb7d4 70%,#d9e2ea 100%)}
.hero-title{left:80px;top:322px;font-size:50px}
.hero-sub{left:80px;top:394px;width:420px;font-size:24px;font-style:italic;font-weight:700;color:var(--ocean);line-height:35px}

/* features */
.feature{top:668px;height:135px;width:400px;display:flex;align-items:center;justify-content:center;gap:22px;color:#fff;font-family:'Montserrat',sans-serif;font-weight:600;font-size:19px;text-transform:uppercase;letter-spacing:.5px;line-height:27px}
.feature .ring{width:62px;height:62px;border:2px solid rgba(255,255,255,.8);border-radius:50%;display:flex;align-items:center;justify-content:center}

/* welcome */
.welcome-title{left:0;top:850px;width:1200px;text-align:center;font-size:42px}
.welcome-copy{left:271px;top:915px;width:658px;text-align:center;font-size:14.5px;line-height:25px}
.welcome-copy p+p{margin-top:13px}
.btn{height:46px;border-radius:23px;color:#fff;font-family:'Montserrat',sans-serif;font-weight:600;font-size:15px;letter-spacing:1px;display:flex;align-items:center;justify-content:center;gap:14px;text-transform:uppercase}
.btn-more{left:387px;top:1104px;width:208px;background:linear-gradient(90deg,var(--sky),var(--navy))}
.btn-contact{left:605px;top:1104px;width:208px;background:linear-gradient(90deg,var(--sky),var(--navy))}

/* services */
.services{left:0;top:1230px;width:1200px;height:723px;background:var(--muted)}
.services-photo{left:0;top:1230px;width:580px;height:640px;background:linear-gradient(135deg,#1d8fe0,#1463c2);clip-path:polygon(0 0,100% 0,0 100%)}
.services-title{left:582px;top:1306px;font-size:42px}
.services-sub{left:582px;top:1366px;width:540px;font-size:16px;font-style:italic;line-height:26px;color:#333}
.service{width:270px}
.service svg{display:block;height:48px}
.service h3{font-family:'Montserrat',sans-serif;font-weight:600;font-size:21px;color:var(--ink);margin-top:12px}
.service p{font-size:14.5px;line-height:24px;margin-top:8px}
.service a{display:inline-flex;align-items:center;gap:10px;margin-top:8px;font-size:13px;color:var(--ocean);text-decoration:underline;letter-spacing:.5px}

/* testimonials */
.testimonials{left:0;top:1953px;width:1200px;height:457px;background:linear-gradient(90deg,var(--sky),var(--navy))}
.testimonials-title{left:0;top:2008px;width:1200px;text-align:center;font-size:40px;color:#fff}
.avatar{left:553px;top:2096px;width:94px;height:94px;border-radius:50%;background:#d7dde3;border:4px solid #fff}
.quote-mark{left:542px;top:2150px;width:32px;height:32px;border-radius:50%;background:#fff;color:var(--ocean);font-family:'Montserrat',sans-serif;font-weight:700;font-size:26px;text-align:center;line-height:38px}
.client-name{left:0;top:2222px;width:1200px;text-align:center;color:#fff;font-family:'Montserrat',sans-serif;font-weight:600;font-size:21px}
.client-quote{left:245px;top:2265px;width:710px;text-align:center;color:#fff;font-style:italic;font-size:15px;line-height:26px}
.arrow{top:2191px;width:50px;height:50px;border-radius:50%;display:flex;align-items:center;justify-content:center}
.arrow-prev{left:75px;background:rgba(255,255,255,.25)}
.arrow-next{left:1069px;background:#fff}

/* gallery */
.gallery-title{left:0;top:2456px;width:1200px;text-align:center;font-size:40px}
.tile{background:linear-gradient(135deg,#7f9a6f,#b0a590)}

/* contact */
.call-band{left:0;top:3243px;width:602px;height:103px;background:linear-gradient(90deg,var(--ocean),var(--sky));display:flex;align-items:center;justify-content:center;gap:24px;color:#fff;font-family:'Montserrat',sans-serif;font-weight:600;font-size:30px}
.call-band .ring{width:50px;height:50px;border:2px solid #fff;border-radius:50%;display:flex;align-items:center;justify-content:center}
.van-photo{left:0;top:3346px;width:602px;height:356px;background:linear-gradient(180deg,#7f9c78 0%,#c8cdd1 45%,#9ea3a6 100%)}
.touch{left:602px;top:3243px;width:598px;height:459px;background:var(--field)}
.touch-title{left:675px;top:3296px;font-size:40px;font-weight:600;color:#222}
.field{height:48px;border:1.5px solid var(--line);background:var(--field);font-size:14px;color:#666;padding:14px 14px}
.submit{left:675px;top:3584px;width:166px;height:48px;border-radius:24px;background:linear-gradient(90deg,var(--sky),var(--navy));color:#fff;font-family:'Montserrat',sans-serif;font-weight:600;font-size:17px;letter-spacing:1px;display:flex;align-items:center;justify-content:center}

/* footer */
.footer{left:0;top:3702px;width:1200px;height:64px;background:linear-gradient(90deg,var(--sky),var(--navy));color:#fff;font-size:14px;display:flex;align-items:center;justify-content:center}
</style>
</head>
<body>

<header>
  <div class="abs topbar">
    <span><svg width="18" height="18" viewBox="0 0 24 24" fill="#fff"><path d="M6.6 10.8a15 15 0 006.6 6.6l2.2-2.2a1 1 0 011-.25 11.4 11.4 0 003.6.6 1 1 0 011 1V20a1 1 0 01-1 1A17 17 0 013 4a1 1 0 011-1h3.5a1 1 0 011 1 11.4 11.4 0 00.6 3.6 1 1 0 01-.25 1z"/></svg>123 456 7890</span>
    <span><svg width="20" height="16" viewBox="0 0 20 16"><rect x="1" y="1" width="18" height="14" fill="#fff"/><path d="M1 1l9 7 9-7" stroke="#1b74c8" stroke-width="1.6" fill="none"/></svg>info@clearflow.com</span>
  </div>
  <div class="abs brand"><i></i>CLEARFLOW</div>
  <nav class="abs nav">
    <span class="on">HOME</span><span>ABOUT</span><span>SERVICES</span><span>TESTIMONIALS</span><span>NEWS</span><span>CONTACT</span>
  </nav>
</header>

<section>
  <div class="abs hero" role="img" aria-label="Photo of a smiling plumber holding a pipe wrench beside a water heater"></div>
  <h1 class="abs heading hero-title">Clearflow</h1>
  <p class="abs hero-sub">Lorem Ipsum is simply dummy text of the printing and typesetting.</p>
</section>

<section>
  <div class="abs feature" style="left:0;background:var(--sky)">
    <div class="ring"><svg width="30" height="22" viewBox="0 0 30 22" fill="none" stroke="#fff" stroke-width="2"><rect x="1" y="1" width="28" height="20" rx="3"/><circle cx="15" cy="11" r="4"/></svg></div>Fair prices
  </div>
  <div class="abs feature" style="left:400px;background:var(--ocean)">
    <div class="ring"><svg width="28" height="28" viewBox="0 0 24 24" fill="none" stroke="#fff" stroke-width="2"><circle cx="12" cy="12" r="3.5"/><path d="M12 2v3M12 19v3M2 12h3M19 12h3M4.9 4.9l2.1 2.1M17 17l2.1 2.1M4.9 19.1L7 17M17 7l2.1-2.1"/></svg></div>Advance<br>technology
  </div>
  <div class="abs feature" style="left:800px;background:var(--navy)">
    <div class="ring"><svg width="28" height="28" viewBox="0 0 24 24" fill="none" stroke="#fff" stroke-width="2"><circle cx="12" cy="12" r="9"/><path d="M12 7v5l3 3"/></svg></div>24/7 opened
  </div>
</section>

<section>
  <h2 class="abs heading welcome-title">Welcome to Clearflow</h2>
  <div class="abs welcome-copy">
    <p>Lorem Ipsum is simply dummy text of the printing and typesetting industry. Lorem Ipsum has been the industry's standard dummy text ever since the 1500s, when an unknown printer took a galley of type and scrambled it to make a type specimen book.</p>
    <p>It has survived not only five centuries, but also the leap into electronic typesetting, remaining essentially unchanged. It was popularised in the 1960s with the release of Lettrafix sheets containing Lorem Ipsum passages, and more recently with desktop publishing software like PageComposer including versions.</p>
  </div>
  <div class="abs btn btn-more">Know more <svg width="18" height="16" viewBox="0 0 18 16" fill="#fff"><path d="M0 7L18 0 14 16 9 10z"/></svg></div>
  <div class="abs btn btn-contact">Contact us <svg width="18" height="16" viewBox="0 0 18 16" fill="#fff"><path d="M0 7L18 0 14 16 9 10z"/></svg></div>
</section>

<section>
  <div class="abs services"></div>
  <div class="abs services-photo" role="img" aria-label="Flat lay of plumbing fittings, faucet, hoses and a wrench on a blue surface"></div>
  <h2 class="abs heading services-title">Services we provide</h2>
  <p class="abs services-sub">Lorem Ipsum is simply dummy text of the printing and typesetting industry. Lorem Ipsum has been the industry's standard dummy text ever.</p>

  <div class="abs service" style="left:580px;top:1452px">
    <svg width="48" height="48" viewBox="0 0 48 48" fill="none" stroke="#1b74c8" stroke-width="2.2"><path d="M14 26V10a3 3 0 016 0v12M20 20V7a3 3 0 016 0v15M26 20V9a3 3 0 016 0v14M32 22v-8a3 3 0 016 0v14c0 10-6 16-14 16s-12-5-15-12l-3-8a3 3 0 015-2l3 6"/></svg>
    <h3>Drain cleaning</h3><p>Lorem Ipsum is simply dummy text of the printing and typesetting industry.</p><a>KNOW MORE <svg width="18" height="10" viewBox="0 0 18 10" fill="none" stroke="#1b74c8" stroke-width="1.6"><path d="M0 5h16M12 1l4 4-4 4"/></svg></a>
  </div>
  <div class="abs service" style="left:873px;top:1452px">
    <svg width="48" height="48" viewBox="0 0 48 48" fill="none" stroke="#1b74c8" stroke-width="2.2"><path d="M30 6a10 10 0 00-9 14L6 35a4 4 0 006 6l15-15a10 10 0 0013-10l-6 5-6-2-2-6 6-5z"/></svg>
    <h3>Repairs</h3><p>Lorem Ipsum is simply dummy text of the printing and typesetting industry.</p><a>KNOW MORE <svg width="18" height="10" viewBox="0 0 18 10" fill="none" stroke="#1b74c8" stroke-width="1.6"><path d="M0 5h16M12 1l4 4-4 4"/></svg></a>
  </div>
  <div class="abs service" style="left:289px;top:1683px">
    <svg width="48" height="48" viewBox="0 0 48 48" fill="none" stroke="#1b74c8" stroke-width="2.2"><rect x="18" y="4" width="12" height="8"/><path d="M6 16h36v10H6zM24 26v6"/><path d="M24 36c-2 3-3 5-3 6a3 3 0 006 0c0-1-1-3-3-6z"/></svg>
    <h3>Leak detection</h3><p>Lorem Ipsum is simply dummy text of the printing and typesetting industry.</p><a>KNOW MORE <svg width="18" height="10" viewBox="0 0 18 10" fill="none" stroke="#1b74c8" stroke-width="1.6"><path d="M0 5h16M12 1l4 4-4 4"/></svg></a>
  </div>
  <div class="abs service" style="left:580px;top:1683px">
    <svg width="48" height="48" viewBox="0 0 48 48" fill="none" stroke="#1b74c8" stroke-width="2.2"><rect x="12" y="8" width="24" height="34" rx="4"/><circle cx="24" cy="22" r="6"/><path d="M18 36h12M8 16h4M36 16h4"/></svg>
    <h3>Thermal</h3><p>Lorem Ipsum is simply dummy text of the printing and typesetting industry.</p><a>KNOW MORE <svg width="18" height="10" viewBox="0 0 18 10" fill="none" stroke="#1b74c8" stroke-width="1.6"><path d="M0 5h16M12 1l4 4-4 4"/></svg></a>
  </div>
  <div class="abs service" style="left:873px;top:1683px">
    <svg width="48" height="48" viewBox="0 0 48 48" fill="none" stroke="#1b74c8" stroke-width="2.2"><rect x="8" y="6" width="22" height="26" rx="2"/><path d="M13 14h12M13 20h12M13 26h8"/><circle cx="32" cy="36" r="8"/><path d="M32 32v4l3 2"/></svg>
    <h3>Methods</h3><p>Lorem Ipsum is simply dummy text of the printing and typesetting industry.</p><a>KNOW MORE <svg width="18" height="10" viewBox="0 0 18 10" fill="none" stroke="#1b74c8" stroke-width="1.6"><path d="M0 5h16M12 1l4 4-4 4"/></svg></a>
  </div>
</section>

<section>
  <div class="abs testimonials"></div>
  <h2 class="abs heading testimonials-title">What our clients say about us</h2>
  <div class="abs avatar" role="img" aria-label="Client portrait"></div>
  <div class="abs quote-mark">“</div>
  <div class="abs client-name">Name Surname</div>
  <p class="abs client-quote">Lorem Ipsum is simply dummy text of the printing and typesetting industry. Lorem Ipsum has been the industry's standard dummy text ever since the 1500s, when an unknown printer took a galley of type and scrambled it to make a type specimen book.</p>
  <div class="abs arrow arrow-prev"><svg width="12" height="18" viewBox="0 0 12 18" fill="none" stroke="#fff" stroke-width="2.4"><path d="M10 2L3 9l7 7"/></svg></div>
  <div class="abs arrow arrow-next"><svg width="12" height="18" viewBox="0 0 12 18" fill="none" stroke="#1b74c8" stroke-width="2.4"><path d="M2 2l7 7-7 7"/></svg></div>
</section>

<section>
  <h2 class="abs heading gallery-title">Work gallery</h2>
  <div class="abs tile" style="left:78px;top:2530px;width:334px;height:251px;background:linear-gradient(180deg,#3f7fd0 0%,#9cc0e6 40%,#e9ecef 60%,#6d9a55 100%)" role="img" aria-label="Two white service vans parked on a driveway"></div>
  <div class="abs tile" style="left:78px;top:2801px;width:334px;height:344px;background:linear-gradient(180deg,#e6e4df,#8c96a0)" role="img" aria-label="Newly installed water heater in a utility closet"></div>
  <div class="abs tile" style="left:434px;top:2530px;width:334px;height:344px;background:linear-gradient(160deg,#6f5e48,#a49784)" role="img" aria-label="Plumber working on a pipe in a crawl space"></div>
  <div class="abs tile" style="left:434px;top:2894px;width:334px;height:251px;background:linear-gradient(160deg,#5a3f2c,#8a6a4f)" role="img" aria-label="Excavated copper water line in soil"></div>
  <div class="abs tile" style="left:791px;top:2530px;width:331px;height:251px;background:linear-gradient(160deg,#4b3a2a,#6c9a4c)" role="img" aria-label="Dug access hole in a lawn with equipment"></div>
  <div class="abs tile" style="left:791px;top:2801px;width:331px;height:344px;background:linear-gradient(180deg,#555a5e,#a8aaa8)" role="img" aria-label="Drain cleaning machine on a garage floor"></div>
</section>

<section>
  <div class="abs call-band">CALL US NOW! <span class="ring"><svg width="22" height="22" viewBox="0 0 24 24" fill="#fff"><path d="M6.6 10.8a15 15 0 006.6 6.6l2.2-2.2a1 1 0 011-.25 11.4 11.4 0 003.6.6 1 1 0 011 1V20a1 1 0 01-1 1A17 17 0 013 4a1 1 0 011-1h3.5a1 1 0 011 1 11.4 11.4 0 00.6 3.6 1 1 0 01-.25 1z"/></svg></span> 123 456 7890</div>
  <div class="abs van-photo" role="img" aria-label="White plumbing service vans parked outside a home"></div>
  <div class="abs touch"></div>
  <h2 class="abs heading touch-title">Get in touch</h2>
  <div class="abs field" style="left:675px;top:3358px;width:216px">Name</div>
  <div class="abs field" style="left:904px;top:3358px;width:218px">Email</div>
  <div class="abs field" style="left:675px;top:3416px;width:216px">Phone</div>
  <div class="abs field" style="left:904px;top:3416px;width:218px">Service</div>
  <div class="abs field" style="left:675px;top:3476px;width:447px;height:88px">Message</div>
  <div class="abs submit">SUBMIT</div>
</section>

<footer class="abs footer">©CLEARFLOW PLUMBING, 2019 - All Rights Reserved.</footer>

</body>
</html>
```